MODERN DESIGN BUSINESS CARDS FOR A CREDIT REPAIR COMPANY

Our goal is to have a modern yet professional business card for our credit repair company. Something that'll catch the eye of our clients. PLEASE BE CREATIVE. WE WOULD LIKE TO SEE HOW THIS WOULD LOOK WITH A WHITE AND BLACK BACK GROUND.

Contact Information for Business Card

THIS WILL BE A DOUBLE SIDED BUSINESS CARD, THE COLORS WE WOULD LIKE TO HAVE IS BLACK, BLUES AND WHITE

Colors
3277b5
33a6d7
ffffff

Requirements
Must have
• MUST HAVE OUR LOGO, BUSINESS PHONE # (482 )607-5731, EXAMPLESOCIAL LINK EXAMPLESOCIAL.TEST/VORMANTHCREDITSOLUTIONS, CALL US FOR YOUR FREE CONSULTATION
Nice to have
• ITEMS WE DELETE: LATE PAYMENTS, CHARGE-OFFS, REPOSESSIONS, HOSPITAL BILLS, STUDENT LOANS, FORECLOSURES, CHILD SUPPORT AND BANKRUPTCIES.

```html
<!DOCTYPE html>
<html lang="en">
<head>
<meta charset="utf-8">
<title>Vormanth Credit Solutions – Business Cards</title>
<link rel="stylesheet" href="https://fonts.googleapis.com/css2?family=Roboto:wght@400;700;900&display=swap">
<style>
  :root {
    --ink: #111214;
    --card-black: #151517;
    --paper: #ffffff;
    --brand-blue: #1b4a86;
    --brand-blue-band: #15457f;
    --link-blue: #2c5a98;
    --stage: #2a2a2c;
    --ghost: #2a2a2d;
  }
  * { box-sizing: border-box; margin: 0; padding: 0; }
  html, body { width: 1200px; height: 880px; overflow: hidden; }
  body {
    background: var(--stage);
    font-family: "Roboto", Arial, sans-serif;
    position: relative;
  }
  .card {
    position: absolute;
    width: 640px;
    height: 366px;
    border-radius: 22px;
    overflow: hidden;
    box-shadow: 0 18px 40px rgba(0,0,0,0.55);
  }

  /* Back side */
  .card-back { left: 120px; top: 44px; background: var(--card-black); color: var(--paper); }
  .card-back .ghost-circle {
    position: absolute; right: -40px; top: -20px;
    width: 360px; height: 360px; border-radius: 50%;
    border: 34px solid var(--ghost);
  }
  .brand { position: absolute; display: flex; align-items: center; gap: 16px; }
  .brand-dot { width: 62px; height: 62px; border-radius: 50%; border: 5px solid currentColor; flex: none; }
  .brand-name { font-weight: 700; line-height: 1; }
  .brand-name .word { display: block; font-size: 40px; letter-spacing: 1px; }
  .brand-name .sub { display: block; font-size: 15px; letter-spacing: 6px; margin-top: 6px; }
  .card-back .brand { left: 48px; top: 62px; color: var(--paper); }

  .delete-list { position: absolute; left: 52px; top: 186px; font-weight: 700; font-size: 19px; line-height: 1.3; text-transform: uppercase; }
  .delete-list h2 { font-size: 19px; font-weight: 700; }
  .delete-list ul { list-style: none; }
  .delete-list li::before { content: "• "; }

  /* Front side */
  .card-front { left: 440px; top: 470px; background: var(--paper); }
  .band { position: absolute; left: 0; width: 100%; display: flex; align-items: center; justify-content: center; flex-direction: column; }
  .band-top { top: 0; height: 140px; }
  .band-black { top: 140px; height: 118px; background: var(--ink); }
  .band-white { top: 258px; height: 56px; }
  .band-blue { top: 314px; height: 52px; background: var(--brand-blue-band); }
  .card-front .brand { position: static; color: var(--brand-blue); }
  .phone { color: var(--paper); font-weight: 700; font-size: 44px; letter-spacing: 1px; }
  .social { color: var(--link-blue); font-size: 19px; font-weight: 400; margin-top: 6px; letter-spacing: 0.3px; }
  .call { color: var(--brand-blue); font-weight: 900; font-size: 38px; }
  .consult { color: var(--paper); font-weight: 700; font-size: 28px; letter-spacing: 0.5px; }
</style>
</head>
<body>
  <section class="card card-back" aria-label="Card back">
    <div class="ghost-circle"></div>
    <div class="brand">
      <span class="brand-dot"></span>
      <span class="brand-name"><span class="word">VORMANTH</span><span class="sub">CREDIT SOLUTIONS</span></span>
    </div>
    <div class="delete-list">
      <h2>Items we delete</h2>
      <ul>
        <li>Late payments</li>
        <li>Charge-offs</li>
        <li>Reposessions</li>
        <li>Hospital bills, student loans</li>
        <li>Foreclosures, child support</li>
        <li>and bankruptcies.</li>
      </ul>
    </div>
  </section>

  <section class="card card-front" aria-label="Card front">
    <div class="band band-top">
      <div class="brand">
        <span class="brand-dot"></span>
        <span class="brand-name"><span class="word">VORMANTH</span><span class="sub">CREDIT SOLUTIONS</span></span>
      </div>
    </div>
    <div class="band band-black">
      <p class="phone">(482) 607-5731</p>
      <p class="social">EXAMPLESOCIAL.TEST/VORMANTHCREDITSOLUTIONS</p>
    </div>
    <div class="band band-white"><p class="call">CALL US</p></div>
    <div class="band band-blue"><p class="consult">FOR YOUR FREE CONSULTATION</p></div>
  </section>
</body>
</html>
```